KORVEL's Sponsorship Showcase Brochure

We're on the hunt for an adept graphic designer to design a 2-4 page brochure that compellingly showcases the sponsorship opportunities at KORVEL, a state-of-the-art, non-profit facility owned by the City of Brandmere, OK. This won't be your typical folding brochure but rather 2-4 full pages of engaging visuals and content. At KORVEL, we're more than just a hub for aerospace, defense, and related industries. We're champions of STEM education and connectors between academia and the industry.

Our aim with this brochure is to vividly detail spaces like our convention rooms, conference areas, and outdoor reception zones available for naming rights. Additionally, the specifics of sponsorship levels and their associated costs can be found in the attached Excel file. Ultimately, we want to pique the interest of local businesses, presenting them with these unique, tax-deductible sponsorship opportunities and inspiring them to step forward as key financial sponsors, strengthening our shared dedication to progress and community betterment. The final page of the brochure should guide readers on how to sign up and become a part of our mission.

Target Market(s)

Local businesses in Lawton, OK

Industry/Entity Type

Commercial Real Estate, Community Development

Font styles to use
Sans Serif

Colors
EB3D1F
EC4F4E
F09395
F8D3D4
FCEDEE

Requirements
Must have
• The project requires a 2-4 page non-folding brochure showcasing KORVEL's sponsorship opportunities, detailing the benefits, referencing the attached Excel for sponsorship levels and costs, and providing sign-up instructions on the final page.

```html
<!DOCTYPE html>
<html lang="en">
<head>
<meta charset="UTF-8">
<title>KORVEL Sponsorship Showcase – Outdoor Reception Area</title>
<link href="https://fonts.googleapis.com/css2?family=Urbanist:ital,wght@0,400;0,500;0,700;1,300;1,700&display=swap" rel="stylesheet">
<style>
  :root {
    --blush: #FCEDEE;
    --flame: #EB3D1F;
    --gold: #F2B01E;
    --ink-light: #FCEDEE;
    --photo-warm: #9a8a7c;
    --photo-cool: #5e6a74;
  }
  * { margin: 0; padding: 0; box-sizing: border-box; }
  html, body { width: 900px; height: 1200px; overflow: hidden; }
  body { font-family: "Urbanist", sans-serif; background: var(--flame); }
  .page { position: relative; width: 900px; height: 1200px; overflow: hidden; }

  /* Conference room benefits band */
  .conference-band { position: absolute; left: 0; top: 0; width: 900px; height: 307px; background: var(--blush); }
  .section-heading { position: absolute; color: var(--gold); line-height: 1.05; }
  .section-heading .kicker { display: block; font-style: italic; font-weight: 300; font-size: 26px; }
  .section-heading .main { display: block; font-weight: 500; font-size: 36px; line-height: 1.08; }
  .conference-band .section-heading { left: 26px; top: 86px; }
  .divider { position: absolute; }
  .conference-band .divider { left: 274px; top: 59px; width: 8px; height: 201px; background: var(--gold); }
  .benefit-list { position: absolute; list-style: none; font-size: 14.6px; line-height: 16.8px; }
  .conference-band .benefit-list { left: 308px; top: 41px; width: 560px; color: var(--gold); }
  .conference-band .benefit-list li { margin-bottom: 4px; }
  .benefit-list strong { font-weight: 700; }

  /* Outdoor reception area */
  .area-title { position: absolute; left: 288px; top: 332px; color: var(--ink-light); font-style: italic; font-weight: 700; font-size: 54px; line-height: 49px; letter-spacing: 1px; }
  .area-tagline { position: absolute; left: 432px; top: 445px; width: 270px; color: var(--gold); font-weight: 700; font-size: 16px; line-height: 23px; }
  .photo { position: absolute; }
  .photo-mingling { left: 42px; top: 396px; width: 234px; height: 234px; background: linear-gradient(160deg, #b9b3ab, var(--photo-warm) 55%, #4c4a4c); }
  .photo-lounge { left: 135px; top: 495px; width: 233px; height: 233px; background: linear-gradient(170deg, #6d7478, var(--photo-cool) 45%, #a79c90); }

  .features-heading { position: absolute; left: 38px; top: 690px; color: var(--ink-light); font-weight: 500; font-size: 41px; line-height: 46px; }
  .feature-list { position: absolute; left: 28px; top: 793px; width: 410px; list-style: none; font-size: 14.6px; line-height: 16.8px; color: var(--gold); }
  .feature-list li { margin-bottom: 8px; }
  .feature-list strong { color: var(--ink-light); font-weight: 700; }

  .reception-benefits .section-heading { left: 480px; top: 584px; }
  .reception-benefits .divider { left: 446px; top: 705px; width: 9px; height: 460px; background: var(--ink-light); }
  .reception-benefits .benefit-list { left: 469px; top: 724px; width: 410px; color: var(--ink-light); }
  .reception-benefits .benefit-list li { margin-bottom: 10px; }
  .reception-benefits .benefit-list strong { color: var(--gold); }
</style>
</head>
<body>
<main class="page">
  <section class="conference-band">
    <h2 class="section-heading"><span class="kicker">Benefits of</span><span class="main">Naming Rights<br>Sponsorship</span></h2>
    <div class="divider"></div>
    <ul class="benefit-list">
      <li><strong>Prominent Brand Exposure:</strong> Your company’s name and logo will take center stage as the official naming rights sponsor of the KORVEL Conference Room, ensuring high visibility during corporate meetings and presentations.</li>
      <li><strong>Professional Reputation:</strong> Align your brand with a space that epitomizes professionalism, innovation, and privacy, enhancing your company’s image as a supporter of high-level discussions.</li>
      <li><strong>Networking Opportunities:</strong> Access exclusive corporate events hosted in this space, providing unique opportunities to connect with business leaders, decision-makers, and industry influencers.</li>
      <li><strong>Privacy Assurance:</strong> Showcase your commitment to ensuring confidential discussions and presentations have a secure and private environment.</li>
      <li><strong>Legacy of Excellence:</strong> Associate your brand with a space that represents cutting-edge technology and fosters successful corporate interactions.</li>
    </ul>
  </section>

  <section class="outdoor-reception">
    <h1 class="area-title">OUTDOOR<br>RECEPTION<br>AREA</h1>
    <p class="area-tagline">Where Innovation Meets Privacy and Excellence</p>
    <div class="photo photo-mingling" role="img" aria-label="Photo of professionals mingling with drinks under an outdoor canopy"></div>
    <div class="photo photo-lounge" role="img" aria-label="Photo of guests chatting on outdoor lounge couches around a wooden table"></div>

    <h2 class="features-heading">Key<br>Features</h2>
    <ul class="feature-list">
      <li><strong>Comfortable Seating:</strong> Enjoy the relaxed atmosphere of our deep seating couches, providing the perfect setting for casual conversations and networking.</li>
      <li><strong>Versatile Bar Area:</strong> Our well-equipped bar area allows for the serving of refreshments, making it an ideal spot for unwinding and connecting with fellow attendees.</li>
      <li><strong>Outdoor Heating:</strong> Stay cozy and comfortable year-round with outdoor heating, ensuring that your events are enjoyable in any weather.</li>
      <li><strong>Entertainment Options:</strong> Challenge your peers to friendly games of ping pong or pool, adding a layer of excitement and engagement to your gatherings.</li>
    </ul>

    <div class="reception-benefits">
      <h2 class="section-heading"><span class="kicker">Benefits of</span><span class="main">Naming Rights<br>Sponsorship</span></h2>
      <div class="divider"></div>
      <ul class="benefit-list">
        <li><strong>Prominent Brand Exposure:</strong> Your company’s name and logo will be prominently displayed as the official naming rights sponsor of the KORVEL Outdoor Reception Area, ensuring high visibility during networking events and receptions.</li>
        <li><strong>Networking Opportunities:</strong> Access exclusive networking events hosted in this space, providing unique opportunities to connect with professionals, event organizers, and industry leaders.</li>
        <li><strong>Community Engagement:</strong> Demonstrate your commitment to fostering connections within the community by supporting a space designed for meaningful interactions.</li>
        <li><strong>Versatile Use:</strong> The KORVEL Outdoor Reception Area will host a wide range of events, offering your company exposure to diverse audiences and industries.</li>
        <li><strong>Enhanced Brand Image:</strong> Align your brand with a space that promotes relaxation, networking, and leisure, enhancing your company’s image as a supporter of work-life balance.</li>
      </ul>
    </div>
  </section>
</main>
</body>
</html>
```